メルマガ登録者募集のためのランディングページのヘッダーデザインをお願いします。
キャッチコピーは以下になります。変わる可能性がありますので文字修正は簡単にできるようにお願いします。
自分に自信が持てない、変わらなければ・・・
と思って悩んでいる方へ

あなたはもう頑張らなくていいのです!

大切なことは『あなたがどう思うか?』
苦しいことを全部やめれば全てうまくいく

1日たった10秒のチャネリングで
生きがい・お金・愛情を全部引き寄せる!
マインドをシフトチェンジするメソッド
を無料で公開します!
• 957×1300
シンプル 複雑
単色 カラフル
暗い 明るい
日常 高級
遊び心 厳粛
未来的 伝統的
女性的 男性的
赤系、茶系、黄・オレンジ系
• 高解像度JPG (.jpg)
• フォトショップ形式 (.psd)
• PNG形式 (.png)
・当LPを閲覧する人の80%程度はスマホでの閲覧と想定されます。スマホで閲覧しても、PCからの閲覧でも、どちらでもきれいに表示されるようにお願い致します。
・文字は太文字、色、大きさなど強弱を付けてインパクトがあるようにお願いします。
・文字はスマートフォンでも読みやすいように限界まで大きくしてください。
・文字の大きさや強調は、ワードファイルに合わせてください。
ワードファイルが添付できません。
以下のURLから見れますでしょうか?

https://cdn.korimadocs.net/v/q48.5193-07/83150927_4208716395827104_7061249382716093841_n.docx/%E5%8E%9F%E7%A8%BF%E8%B3%87%E6%96%99%E3%81%AE%E3%83%87%E3%83%BC%E3%82%BF%E4%B8%80%E8%A6%A7.docx?oh=91c7e0b2f4a8d6350b2e7c91d4f0a6b8&oe=7C394A58&dl=1
色は、ピンク系や暖色系など、女性が好きそうな柔らかいイメージでお願いします。
お世話になります。
後日追記しました、ワードファイルのURLですが、期限切れで見れないようです。
改めて、ファイルを添付してみました。
確認できますでしょうか?
どうぞよろしくお願い致します。
お世話になります。
提案数を増やしたいので3日間の延長をお願いします。
よろしくお願い致します。
度々の追記、申し訳ございません。
添付のワードファイルは下から2列目の文章が
『感情をシフトチェンジするメソッド』となっていますが、
『感情』を『マインド』に変更していただき、
『マインドをシフトチェンジするメソッド』
でお願いします。
『感情』 → 『マインド』です。よろしくお願い致します。

一目見て、パッと目を引くデザインでした。
全体的なバランスもとても良く、色使いや曲線がとても柔らかいイメージで大満足のデザインでした。
本当にありがとうございました。

この度は、沢山のご提案をいただき、ありがとうございました。
私には出来ない仕事なので、皆さまには感謝の気持ちでいっぱいです。
貴重なお時間を頂き、本当にありがとうございました。
また、機会がありましたら、その時はどうぞよろしくお願い致します。

```html
<!DOCTYPE html>
<html lang="ja">
<head>
<meta charset="UTF-8">
<title>マインドをシフトチェンジするメソッド</title>
<link rel="stylesheet" href="https://fonts.googleapis.com/css2?family=Noto+Serif+JP:wght@700;900&family=Great+Vibes&display=swap">
<style>
  :root {
    --band-pink: #e86f86;
    --bg-light: #fbe3e6;
    --bg-mid: #f6c9cf;
    --bg-deep: #f1b3bc;
    --ink: #3b2a2c;
    --accent-red: #c9324f;
    --title-pink: #e2607c;
    --ribbon: #e55a78;
    --white: #ffffff;
    --script: #b88a92;
    --dot: #d9576f;
  }
  html, body {
    margin: 0;
    padding: 0;
    width: 1200px;
    height: 883px;
    overflow: hidden;
  }
  .header {
    position: relative;
    width: 1200px;
    height: 883px;
    overflow: hidden;
    font-family: "Noto Serif JP", serif;
    background:
      radial-gradient(ellipse 420px 260px at 330px 470px, rgba(255,255,255,0.85), rgba(255,255,255,0) 70%),
      radial-gradient(circle at 20% 20%, var(--bg-light), transparent 60%),
      linear-gradient(160deg, var(--bg-light) 0%, var(--bg-mid) 55%, var(--bg-deep) 100%);
  }
  .top-band {
    position: absolute;
    left: 0; top: 0;
    width: 100%;
    height: 48px;
    background: var(--band-pink);
    color: var(--white);
    font-size: 22px;
    font-weight: 700;
    line-height: 48px;
    text-align: center;
    letter-spacing: 0.04em;
    padding-right: 40px;
    box-sizing: border-box;
  }
  .portrait {
    position: absolute;
    left: 770px; top: 175px;
    width: 430px; height: 708px;
    background: linear-gradient(180deg, #f3d6d6 0%, #e9e4e2 45%, #5a5558 75%, #4a4648 100%);
    border-radius: 200px 200px 0 0;
  }
  .headline {
    position: absolute;
    left: 66px; top: 96px;
    width: 1100px;
    height: 70px;
    margin: 0;
    background: rgba(255,255,255,0.9);
    border-radius: 35px;
    color: var(--ink);
    font-size: 52px;
    font-weight: 900;
    line-height: 70px;
    text-align: center;
    letter-spacing: 0.02em;
  }
  .subline {
    position: absolute;
    left: 104px;
    margin: 0;
    color: var(--ink);
    font-size: 30px;
    font-weight: 700;
    line-height: 38px;
    padding-bottom: 2px;
    border-bottom: 3px dotted var(--dot);
    white-space: nowrap;
  }
  .subline--first { top: 178px; }
  .subline--second { top: 226px; }
  .lead {
    position: absolute;
    left: 64px; top: 322px;
    margin: 0;
    color: var(--accent-red);
    font-size: 34px;
    font-weight: 900;
    line-height: 50px;
    white-space: nowrap;
    paint-order: stroke fill;
    -webkit-text-stroke: 6px var(--white);
  }
  .lead .num { font-size: 46px; }
  .ribbon {
    position: absolute;
    left: 60px; top: 320px;
    width: 680px; height: 270px;
  }
  .promise {
    position: absolute;
    left: 76px;
    margin: 0;
    color: var(--ink);
    font-weight: 900;
    white-space: nowrap;
    paint-order: stroke fill;
    -webkit-text-stroke: 10px var(--white);
  }
  .promise--line1 { top: 380px; font-size: 68px; line-height: 86px; }
  .promise--line2 { top: 468px; font-size: 88px; line-height: 104px; }
  .method {
    position: absolute;
    left: 68px; top: 600px;
    margin: 0;
    color: var(--title-pink);
    font-size: 74px;
    font-weight: 900;
    font-style: italic;
    line-height: 84px;
    white-space: nowrap;
    paint-order: stroke fill;
    -webkit-text-stroke: 8px var(--white);
  }
  .method span { display: block; }
  .script-label {
    position: absolute;
    left: 486px; top: 606px;
    color: var(--script);
    font-family: "Great Vibes", cursive;
    font-size: 48px;
    transform: rotate(-6deg);
    white-space: nowrap;
  }
  .free-badge {
    position: absolute;
    left: 408px; top: 788px;
    width: 336px; height: 58px;
    background: var(--ribbon);
    border-radius: 29px;
    color: var(--white);
    font-size: 27px;
    font-weight: 700;
    line-height: 58px;
    text-align: center;
  }
</style>
</head>
<body>
  <header class="header">
    <p class="top-band">自分に自信が持てない、変わらなければ・・・と思って悩んでいる方へ</p>

    <div class="portrait" role="img" aria-label="笑顔で立つ講師の女性の写真"></div>

    <h1 class="headline">＼ あなたはもう頑張らなくていいのです！／</h1>
    <p class="subline subline--first">大切なことは『あなたがどう思うか？』</p>
    <p class="subline subline--second">苦しいことを全部やめれば全てうまくいく!</p>

    <svg class="ribbon" viewBox="0 0 680 270" aria-hidden="true">
      <polygon points="0,10 24,0 24,48 0,58" fill="var(--ribbon)"/>
      <polygon points="640,200 680,188 680,250 640,262" fill="var(--ribbon)"/>
    </svg>

    <p class="lead">＼1日たった<span class="num">10</span>秒のチャネリングで／</p>
    <p class="promise promise--line1">生きがい･お金･愛情を</p>
    <p class="promise promise--line2">全部引き寄せる!</p>

    <span class="script-label">Mind Change</span>
    <h2 class="method">
      <span>マインドを</span>
      <span>シフトチェンジする</span>
      <span>メソッド</span>
    </h2>
    <p class="free-badge">無料で公開します！</p>
  </header>
</body>
</html>
```